New Wrestling company needs a website

We need a website design for a new wrestling company in Australia that will be running 3-4 events per year. Wrestling company is Coralline Elite Grappling (CEG).

The design of the logo is in place and can be provided, and I have purchased the website domain.

A detailed description of the intent and purpose of this company can be provided.

The aim would be to have around 5 specific pages on CEG, with two standard “about” and “contact” pages. E.g.
- About CEG (focus and purpose of the company)
- CEG Events (specific focus on events run by CEG)
- CEG News (news and stories on wrestling’s across Oceania)
- CEG Media (where to watch CEG and our partners))
- CEG Partners and Sponsors (partner and affiliate information)
- CEG Power Rankings (top 10 ranked wrestlers from Oceania which is updated weekly)
- CEG fans (highlighting how to become part of CEG as a fan)
- Contact CEG
Updates

The logo design should now be included in the brief, please feel free to reach out to me directly if you can't access it or require any other information.

Target Market(s)

Wrestling Fans

Industry/Entity Type

Sport / Wrestling

Coding

Coded - Design and coding required

Number of Pages Required

5+ page

Requirements
Must have
• A Wrestling and or Sports feel to the website design

```html
<!DOCTYPE html>
<html lang="en">
<head>
<meta charset="UTF-8">
<title>Coralline Elite Grappling</title>
<link href="https://fonts.googleapis.com/css2?family=Roboto:wght@400;500;700;900&display=swap" rel="stylesheet">
<style>
:root{
  --blue:#2a6fc9;
  --blue-dark:#1d5fb8;
  --ink:#111111;
  --text:#555a60;
  --black:#000000;
  --white:#ffffff;
  --soft:#f3f4f8;
  --line:#2b2b2b;
}
*{margin:0;padding:0;box-sizing:border-box}
html,body{width:1200px;height:3979px;overflow:hidden}
body{font-family:'Roboto',sans-serif;color:var(--ink);background:var(--white);position:relative}
section,header,footer{position:absolute;left:0;width:1200px}
.abs{position:absolute}
.btn{position:absolute;display:flex;align-items:center;justify-content:center;background:var(--blue);color:var(--white);font-weight:500;font-size:16px;border-radius:26px;letter-spacing:.2px}
.photo{position:absolute}
.section-title{position:absolute;left:0;width:1200px;text-align:center;font-weight:700;font-size:42px;letter-spacing:.3px;color:var(--ink)}

/* header */
.site-header{top:0;height:85px;background:var(--black)}
.brand{position:absolute;left:111px;top:22px;display:flex;align-items:center;gap:10px;color:var(--white);font-weight:900;font-size:30px}
.brand .dot{width:34px;height:34px;border-radius:50%;background:var(--blue)}
.main-nav{position:absolute;right:112px;top:33px;display:flex;gap:32px;color:var(--white);font-size:16px;font-weight:500}

/* hero */
.hero{top:85px;height:625px}
.hero-photo{left:0;top:0;width:1200px;height:625px;background:radial-gradient(ellipse at 60% 35%,#6b6a62 0%,#2d3542 40%,#0f1622 80%)}
.hero-title{position:absolute;left:116px;top:170px;color:var(--white);font-weight:900;line-height:1}
.hero-title .l1{font-size:80px;display:block}
.hero-title .l2{font-size:48px;display:block;margin-top:6px}
.hero-text{position:absolute;left:118px;top:313px;width:380px;color:var(--white);font-size:16px;line-height:26px}
.hero-arrow{position:absolute;top:285px}
.dots{position:absolute;top:573px;left:550px;display:flex;gap:16px}
.dots span{width:12px;height:12px;border-radius:50%;background:#9aa0a8}
.dots span.on{background:var(--white)}

/* about */
.about{top:710px;height:607px}
.about-photo{left:111px;top:83px;width:472px;height:439px;background:linear-gradient(135deg,#dcdcdc,#3a3a3e 55%,#1b1b1e);border-radius:3px}
.about h2{position:absolute;left:664px;top:98px;font-size:38px;font-weight:700}
.about .rule{position:absolute;left:664px;top:152px;width:85px;height:4px;background:var(--blue)}
.about p{position:absolute;left:664px;top:180px;width:425px;font-size:15px;line-height:30px;color:var(--text);text-align:justify}

/* events */
.events{top:1317px;height:671px;background:var(--soft)}
.card{position:absolute;background:var(--white);border-radius:4px;box-shadow:0 2px 10px rgba(0,0,0,.08)}
.event-main{left:139px;top:146px;width:444px;height:450px}
.event-main .photo{left:7px;top:7px;width:430px;height:291px;background:linear-gradient(160deg,#1a1a22,#6a4a36 50%,#1a1f2e)}
.event-title{font-weight:700;font-size:16px;color:var(--ink)}
.meta{font-size:13.5px;color:var(--blue);display:flex;align-items:center;gap:6px}
.meta .sep{color:var(--text);margin:0 4px}
.event-main .event-title{position:absolute;top:317px;width:100%;text-align:center}
.event-main .meta{position:absolute;top:346px;width:100%;justify-content:center}
.event-main .desc{position:absolute;top:374px;left:25px;right:25px;text-align:center;font-size:14px;line-height:22px;color:var(--text)}
.event-side{left:619px;width:443px;height:137px}
.event-side .photo{left:8px;top:8px;width:153px;height:121px}
.event-side .event-title{position:absolute;left:176px;top:18px}
.event-side .meta{position:absolute;left:176px;top:43px}
.event-side .desc{position:absolute;left:176px;top:72px;width:240px;font-size:14px;line-height:20px;color:var(--text)}

/* news */
.news{top:1988px;height:614px}
.news-card{position:absolute;top:155px;width:312px;height:370px;background:var(--white);box-shadow:0 2px 10px rgba(0,0,0,.09)}
.news-card .photo{left:0;top:0;width:312px;height:195px}
.news-card .event-title{position:absolute;left:23px;top:214px}
.news-card .date{position:absolute;left:23px;top:244px;font-size:14px;color:var(--ink);display:flex;gap:7px;align-items:center}
.news-card .desc{position:absolute;left:23px;top:274px;width:270px;font-size:14px;line-height:22px;color:var(--text)}
.news-card .more{position:absolute;left:23px;top:330px;font-size:15px;font-weight:700;color:var(--blue);display:flex;align-items:center;gap:7px}

/* sponsors */
.sponsors{top:2602px;height:283px;background:var(--soft)}
.sponsor{position:absolute;top:138px;width:166px;height:85px;background:var(--white);border-radius:4px;box-shadow:0 1px 6px rgba(0,0,0,.07);display:flex;align-items:center;justify-content:center;gap:7px;font-size:21px;font-weight:700;color:#222}
.sponsor .mk{width:16px;height:16px;border-radius:50%;background:#222}
.sponsor-arrow{position:absolute;top:164px;width:34px;height:34px;border-radius:50%;background:var(--white);box-shadow:0 1px 5px rgba(0,0,0,.15);display:flex;align-items:center;justify-content:center}

/* media */
.media{top:2885px;height:767px}
.tile{position:absolute;width:312px;height:254px}
.tile.active{outline:3px solid var(--blue);outline-offset:-3px}

/* footer */
.site-footer{top:3652px;height:327px;background:var(--black);color:var(--white)}
.f-brand{position:absolute;left:141px;top:85px;display:flex;align-items:center;gap:8px;font-weight:900;font-size:28px}
.f-brand .dot{width:30px;height:30px;border-radius:50%;background:var(--blue)}
.f-head{position:absolute;top:62px;font-size:21px;font-weight:700}
.f-links{position:absolute;top:105px;list-style:none;font-size:14px;line-height:21.5px}
.f-links li::before{content:"»";margin-right:14px;font-size:13px}
.f-input{position:absolute;left:669px;top:106px;width:233px;height:42px;border-radius:21px;background:var(--white);color:#444;font-size:13px;display:flex;align-items:center;justify-content:center}
.f-btn{position:absolute;left:669px;top:158px;width:233px;height:42px;border-radius:21px;background:var(--blue);color:var(--white);font-size:14px;font-weight:500;display:flex;align-items:center;justify-content:center}
.social{position:absolute;left:973px;top:105px;list-style:none;font-size:14px;line-height:21.5px}
.social li{display:flex;align-items:center;gap:12px}
.social li span{width:9px;height:9px;background:var(--white)}
.f-rule{position:absolute;left:111px;top:280px;width:978px;height:1px;background:var(--line)}
.copyright{position:absolute;top:292px;width:1200px;text-align:center;font-size:14px}
</style>
</head>
<body>

<header class="site-header">
  <div class="brand"><span class="dot"></span>CEG</div>
  <nav class="main-nav">
    <span>About CEG</span><span>Events</span><span>News</span><span>Media</span><span>Partners</span><span>Power Rankings</span><span>Fans</span><span>Contact</span>
  </nav>
</header>

<section class="hero">
  <div class="photo hero-photo" role="img" aria-label="Masked wrestler leaping in an arena ring under stadium lights"></div>
  <svg class="hero-arrow" style="left:70px" width="26" height="44" viewBox="0 0 26 44"><path d="M23 2 3 22l20 20" fill="none" stroke="#fff" stroke-width="2"/></svg>
  <svg class="hero-arrow" style="left:1102px" width="26" height="44" viewBox="0 0 26 44"><path d="M3 2l20 20L3 42" fill="none" stroke="#fff" stroke-width="2"/></svg>
  <h1 class="hero-title"><span class="l1">CORALLINE</span><span class="l2">ELITE GRAPPLING</span></h1>
  <p class="hero-text">Lorem ipsum dolor sit amet, consectetu adipiscing elit, sed do eiusmod tempor incididunt</p>
  <div class="btn" style="left:118px;top:389px;width:175px;height:50px">GET STARTED</div>
  <div class="dots"><span></span><span class="on"></span><span></span><span></span></div>
</section>

<section class="about">
  <div class="photo about-photo" role="img" aria-label="Two wrestlers grappling on the mat"></div>
  <h2>ABOUT CEG</h2>
  <div class="rule"></div>
  <p>Lorem ipsum dolor sit amet, consectetur adipiscing elit, sed do eiusmod tempor incididunt ut labo et dolore magna aliqua. Quis ipsum suspendisse ults gravida. Risus commodo viverra maecenas accumsan lacus vel facilisis. Lorem ipsum dolor sit amet, consectetur aing elit, sed do eiusmod tempor incididunt ut labo et dolore magna aliqua. Quis ipsum suspendisse ults gravida. Risus commodo viverra maecenas accumsan lacus vel facilisis.</p>
  <div class="btn" style="left:664px;top:446px;width:175px;height:51px">LEARN MORE</div>
</section>

<section class="events">
  <h2 class="section-title" style="top:66px">UPCOMING EVENTS</h2>
  <article class="card event-main">
    <div class="photo" role="img" aria-label="Two wrestlers locked up against the ring ropes"></div>
    <div class="event-title">Finibus Bonorum et Malorum</div>
    <div class="meta">▦ Nov 28, 2021 <span class="sep">|</span> ◷ 2:45 PM</div>
    <p class="desc">Sed ut perspiciatis unde omnis iste natus error sit accusan-tium doloremque laudantium,</p>
  </article>
  <article class="card event-side" style="top:146px">
    <div class="photo" role="img" aria-label="Wrestler leaning on ring ropes" style="background:linear-gradient(135deg,#2a2a2a,#8a5a3c,#101010)"></div>
    <div class="event-title">Finibus Bonorum et Malorum</div>
    <div class="meta">▦ Dec 4, 2021 <span class="sep">|</span> ◷ Sam Keller</div>
    <p class="desc">Sed ut perspiciatis unde omnis iste natus error sit voluptatem accusan-</p>
  </article>
  <article class="card event-side" style="top:303px">
    <div class="photo" role="img" aria-label="Wrestler lifting opponent in a throw" style="background:linear-gradient(135deg,#1d2a4a,#6a3a4a,#1b2030)"></div>
    <div class="event-title">Finibus Bonorum et Malorum</div>
    <div class="meta">▦ Dec 5, 2020 <span class="sep">|</span> ◷ Sam Keller</div>
    <p class="desc">Sed ut perspiciatis unde omnis iste natus error sit voluptatem accusan-</p>
  </article>
  <article class="card event-side" style="top:459px">
    <div class="photo" role="img" aria-label="Masked wrestler in red posing" style="background:linear-gradient(135deg,#0e2a3a,#7a1a1a,#14202a)"></div>
    <div class="event-title">Finibus Bonorum et Malorum</div>
    <div class="meta">▦ Dec 11, 2021 <span class="sep">|</span> ◷ Sam Keller</div>
    <p class="desc">Sed ut perspiciatis unde omnis iste natus error sit voluptatem accusan-</p>
  </article>
</section>

<section class="news">
  <h2 class="section-title" style="top:82px;font-size:34px">RECENT NEWS</h2>
  <article class="news-card" style="left:111px">
    <div class="photo" role="img" aria-label="Empty wrestling ring under spotlights" style="background:linear-gradient(180deg,#1a1a1a,#6a6a6a 60%,#2a2a2a)"></div>
    <div class="event-title">The standard Lorem Ipsum passage</div>
    <div class="date">▦ Nov 22, 2021</div>
    <p class="desc">Lorem ipsum dolor sit amet, consectetur adipiscing elit, sed do eiusmod</p>
    <div class="more">READ MORE <svg width="14" height="14" viewBox="0 0 14 14"><circle cx="7" cy="7" r="7" fill="#2a6fc9"/><path d="M5 4l3 3-3 3" stroke="#fff" stroke-width="2" fill="none"/></svg></div>
  </article>
  <article class="news-card" style="left:444px">
    <div class="photo" role="img" aria-label="Wrestlers mid-move in the ring" style="background:linear-gradient(160deg,#2a3a5a,#b07a5a 50%,#2a2a2a)"></div>
    <div class="event-title">The standard Lorem Ipsum passage</div>
    <div class="date">▦ Nov 15, 2021</div>
    <p class="desc">Lorem ipsum dolor sit amet, consectetur adipiscing elit, sed do eiusmod</p>
    <div class="more">READ MORE <svg width="14" height="14" viewBox="0 0 14 14"><circle cx="7" cy="7" r="7" fill="#2a6fc9"/><path d="M5 4l3 3-3 3" stroke="#fff" stroke-width="2" fill="none"/></svg></div>
  </article>
  <article class="news-card" style="left:777px">
    <div class="photo" role="img" aria-label="Fighters grappling on a cage mat" style="background:linear-gradient(160deg,#3a3a3a,#6a4a4a 50%,#2a5a6a)"></div>
    <div class="event-title">The standard Lorem Ipsum passage</div>
    <div class="date">▦ Nov 08, 2021</div>
    <p class="desc">Lorem ipsum dolor sit amet, consectetur adipiscing elit, sed do eiusmod</p>
    <div class="more">READ MORE <svg width="14" height="14" viewBox="0 0 14 14"><circle cx="7" cy="7" r="7" fill="#2a6fc9"/><path d="M5 4l3 3-3 3" stroke="#fff" stroke-width="2" fill="none"/></svg></div>
  </article>
</section>

<section class="sponsors">
  <h2 class="section-title" style="top:62px;font-size:34px">FEATURED SPONSOR</h2>
  <div class="sponsor-arrow" style="left:41px"><svg width="10" height="10" viewBox="0 0 10 10"><path d="M7 1 2 5l5 4z" fill="#222"/></svg></div>
  <div class="sponsor" style="left:118px"><span class="mk"></span>Orbitline</div>
  <div class="sponsor" style="left:317px"><span class="mk"></span>Mailcrest</div>
  <div class="sponsor" style="left:515px"><span class="mk"></span>Facetry</div>
  <div class="sponsor" style="left:714px;font-size:17px"><span class="mk"></span>Markwell</div>
  <div class="sponsor" style="left:913px"><span class="mk" style="background:#e53030"></span>Tunnelo</div>
  <div class="sponsor-arrow" style="left:1123px"><svg width="10" height="10" viewBox="0 0 10 10"><path d="M3 1l5 4-5 4z" fill="#222"/></svg></div>
</section>

<section class="media">
  <h2 class="section-title" style="top:78px;font-size:34px">CEG MEDIA</h2>
  <div class="tile" role="img" aria-label="Wrestlers in red and blue grappling in a gym" style="left:111px;top:155px;background:linear-gradient(160deg,#6a7078,#a04a3a 50%,#3a4a6a)"></div>
  <div class="tile active" role="img" aria-label="Wrestling video thumbnail" style="left:444px;top:155px;background:radial-gradient(circle at 50% 40%,#5a6070,#1e2228 75%)">
    <svg class="abs" style="left:126px;top:97px" width="60" height="60" viewBox="0 0 60 60"><circle cx="30" cy="30" r="27" fill="none" stroke="#fff" stroke-width="4"/><path d="M24 18l18 12-18 12z" fill="#fff"/></svg>
  </div>
  <div class="tile" role="img" aria-label="Wrestler pinning opponent with referee watching" style="left:777px;top:155px;background:linear-gradient(160deg,#1a1a1a,#6a5a50 55%,#101010)"></div>
  <div class="tile" role="img" aria-label="Two wrestlers facing off under blue stage light" style="left:111px;top:427px;background:radial-gradient(circle at 40% 40%,#3a5a7a,#0c1420 75%)"></div>
  <div class="tile" role="img" aria-label="College wrestlers locked on the mat" style="left:444px;top:427px;background:linear-gradient(160deg,#c08a5a,#5a4a3a 50%,#a87a5a)"></div>
  <div class="tile" role="img" aria-label="Wrestler with long hair in the ring before a crowd" style="left:777px;top:427px;background:linear-gradient(160deg,#4a5a6a,#2a2a2a 50%,#6a5a4a)"></div>
</section>

<footer class="site-footer">
  <div class="f-brand"><span class="dot"></span>CEG</div>
  <div class="f-head" style="left:336px">QUICK LINKS</div>
  <ul class="f-links" style="left:338px"><li>About CEG</li><li>Events</li><li>News</li><li>Media</li><li>Partners</li><li>Power Rankings</li></ul>
  <ul class="f-links" style="left:485px"><li>Fans</li><li>Contact</li><li>Privacy policy</li><li>Facepage</li></ul>
  <div class="f-head" style="left:667px">STAT CONECTED</div>
  <div class="f-input">Your email</div>
  <div class="f-btn">JOIN NEWSLETTER</div>
  <div class="f-head" style="left:973px">FOLLOW US</div>
  <ul class="social"><li><span></span>Facepage</li><li><span></span>Snapgram</li><li><span></span>Chirper</li><li><span></span>Linkwork</li></ul>
  <div class="f-rule"></div>
  <div class="copyright">Copyright © 2022, Coralline Elite Grappling. All rights reserved.</div>
</footer>

</body>
</html>
```